Quiet Lanterns: Reflections on Tide Charts and Orchard Rituals Among Coastal Villages.

Book cover, spine, and back cover. This is written by Dr. T. HALVERSEN, and will be an educational book for academics, government officials, and the general population.
I'm imagining the outline of a person with am active mind in the middle. It would be overlayed on top of a circular galaxy on the background. On either side, smaller, perhaps in the background would be a cross on one side and a few uaps (ufo) of different shapes on the other (orb, saucer, triangle. ) beneath allnof this would be something symbolizing society - either the earth itself or the skyline of a large city.
By Dr. T. HALVERSEN along the bottom, i presume. (Ai cannot make this, but I've included a few examples nonetheless. )
I assume I will be given the opportunity to write a synopsis on the back cover. I will be self publishing and selling from my website.
Target Market(s)
Academics, professionals, church leaders, government officials, and the general public.
Industry/Entity Type
Professional and community education
Requirements
Must have
- It should look like a ph.d level book. Eye catching but not overly fantastical. (Its an educational book not a comic book)
Should not have
- Not hollywood or fantasy book looking. It should look a graduate school book. The tone is quite serious.

```html
<!DOCTYPE html>
<html lang="en">
<head>
<meta charset="utf-8">
<title>Quiet Lanterns — Dr. T. Halversen</title>
<link rel="stylesheet" href="https://fonts.googleapis.com/css2?family=Cinzel:wght@400;900&family=Tinos:ital@1&display=swap">
<style>
  :root {
    --paper: #ffffff;
    --title-teal: #13343b;
    --title-olive: #4f6121;
    --ink: #111111;
    --rule-olive: #56662a;
    --wash-lavender: #b7ace6;
    --wash-soft: #ece8f8;
    --leaf-green: #bfcd80;
    --leaf-teal: #6f9893;
  }
  * { margin: 0; padding: 0; box-sizing: border-box; }
  html, body {
    width: 800px;
    height: 1200px;
    overflow: hidden;
    background: var(--paper);
  }
  .cover {
    position: relative;
    width: 800px;
    height: 1200px;
    background: var(--paper);
  }
  .title {
    position: absolute;
    left: 0;
    width: 800px;
    text-align: center;
    font-family: "Cinzel", "Trajan Pro", serif;
    font-weight: 900;
    text-transform: uppercase;
    line-height: 1;
    white-space: nowrap;
  }
  .title-line-1 {
    top: 62px;
    font-size: 150px;
    color: var(--title-teal);
  }
  .title-line-2 {
    top: 214px;
    font-size: 116px;
    color: var(--title-olive);
  }
  .rule {
    position: absolute;
    left: 68px;
    width: 664px;
    height: 4px;
    background: linear-gradient(90deg,
      rgba(86,102,42,0) 0%,
      rgba(86,102,42,0.55) 25%,
      var(--rule-olive) 50%,
      rgba(86,102,42,0.55) 75%,
      rgba(86,102,42,0) 100%);
  }
  .rule-top { top: 366px; }
  .rule-bottom { top: 484px; }
  .subtitle {
    position: absolute;
    top: 384px;
    left: 0;
    width: 800px;
    text-align: center;
    font-family: "Tinos", "Times New Roman", serif;
    font-style: italic;
    font-size: 30px;
    line-height: 43px;
    letter-spacing: 1.6px;
    color: var(--ink);
  }
  .artwork {
    position: absolute;
    left: 110px;
    top: 508px;
    width: 580px;
    height: 590px;
  }
  .author {
    position: absolute;
    top: 1098px;
    left: 0;
    width: 800px;
    text-align: center;
    font-family: "Cinzel", "Trajan Pro", serif;
    font-weight: 400;
    font-size: 58px;
    line-height: 1;
    letter-spacing: 4px;
    text-transform: uppercase;
    color: var(--ink);
    white-space: nowrap;
  }
</style>
</head>
<body>
  <main class="cover">
    <h1>
      <span class="title title-line-1">Quiet</span>
      <span class="title title-line-2">Lanterns</span>
    </h1>

    <div class="rule rule-top"></div>
    <p class="subtitle">Reflections on Tide Charts and Orchard Rituals<br>Among Coastal Villages</p>
    <div class="rule rule-bottom"></div>

    <svg class="artwork" viewBox="0 0 580 590" role="img"
         aria-label="Watercolour illustration of a white cross framed by green and teal leaves and gold speckles on a soft lavender wash">
      <defs>
        <radialGradient id="wash" cx="50%" cy="50%" r="50%">
          <stop offset="0%" stop-color="var(--wash-lavender)"/>
          <stop offset="35%" stop-color="var(--leaf-green)"/>
          <stop offset="65%" stop-color="var(--leaf-teal)" stop-opacity="0.75"/>
          <stop offset="85%" stop-color="var(--wash-soft)" stop-opacity="0.8"/>
          <stop offset="100%" stop-color="#ffffff" stop-opacity="0"/>
        </radialGradient>
      </defs>
      <ellipse cx="290" cy="292" rx="285" ry="292" fill="url(#wash)"/>
    </svg>

    <p class="author">Dr. T. Halversen</p>
  </main>
</body>
</html>
```